We are an online mail order nursery selling live plants who needs a 1 page landing page for an upcom

We are opening a new sister site to our main site. The new site is membership based. We need a landing page for an email campaign that is both attention grabbing and simply luring the customer to click on the learn more about Membership Page : http://www.thefernguild.com/pages/membership-info
The landing page will need to have space reserved for a white board presentation. I have attached the video below. The vid will be hosted on You tube so we should be able to use the iframe / embed technique. Again our goal is to funnel the customer to http://www.thefernguild.com/pages/membership-info where they can get more details.

Target Market(s)

Home owners between the age of 35 and 65 - gardening enthusiast

Industry/Entity Type

Campaign

Number of Pages Required

1 page

Font styles to use
Sans Serif

Requirements
Must have
• space to embed white board video

```html
<!DOCTYPE html>
<html lang="en">
<head>
<meta charset="utf-8">
<title>The Fern Guild – Membership</title>
<link href="https://fonts.googleapis.com/css2?family=Lato:wght@400;700;900&display=swap" rel="stylesheet">
<style>
  :root{
    --green:#7dc242;
    --green-dark:#3e7a1a;
    --hero-a:#2f6a12;
    --hero-b:#5a9a24;
    --ink:#222;
    --muted:#777;
    --nav:#666;
    --paper:#f6f6f4;
    --footer:#e6e6e6;
    --wood-a:#7a5a25;
    --wood-b:#a88a4c;
    --purple:#3c2a7a;
    --white:#fff;
  }
  *{margin:0;padding:0;box-sizing:border-box}
  html,body{width:847px;height:1200px;overflow:hidden;background:var(--white)}
  body{position:relative;font-family:'Lato',sans-serif;color:var(--ink)}
  .abs{position:absolute}

  /* header */
  .site-header{position:absolute;left:0;top:0;width:847px;height:88px;background:var(--white)}
  .brand{left:84px;top:28px;display:flex;align-items:center;gap:8px}
  .brand-mark{width:26px;height:26px;border-radius:50%;background:var(--green-dark)}
  .brand-name{font-size:22px;font-weight:700;color:var(--green-dark);letter-spacing:.5px}
  .main-nav{left:454px;top:38px;display:flex;gap:25px;font-size:10.5px;font-weight:700;color:var(--nav)}
  .btn-signup-top{left:680px;top:29px;width:83px;height:32px;background:var(--green);color:var(--white);border-radius:3px;font-size:12.5px;font-weight:700;display:flex;align-items:center;justify-content:center}

  /* hero */
  .hero{position:absolute;left:0;top:88px;width:847px;height:539px;background:radial-gradient(ellipse at 60% 40%,var(--hero-b),var(--hero-a) 75%)}
  .hero-title{left:0;width:847px;top:22px;text-align:center;color:var(--white);font-size:29px;font-weight:900;letter-spacing:8.5px}
  .hero-sub{left:0;width:847px;top:68px;text-align:center;color:var(--white);font-size:12px;font-weight:700;letter-spacing:.8px}
  .video{left:152px;top:104px;width:544px;height:329px;background:var(--white);overflow:hidden}
  .video-art{left:0;top:0;width:544px;height:282px;background:linear-gradient(180deg,#fdfdfd,#eef1f6)}
  .video-caption{left:0;width:544px;top:204px;text-align:center;color:var(--purple);font-weight:900;font-size:25px;line-height:28px;letter-spacing:-.8px}
  .video-bar{left:0;top:282px;width:544px;height:47px;background:rgba(90,90,90,.85)}
  .track-title{left:0;width:544px;top:4px;text-align:center;color:var(--white);font-size:7.5px}
  .time{top:21px;color:#ddd;font-size:6.5px}
  .progress{left:167px;top:24px;width:203px;height:2px;background:#888}
  .progress-fill{left:0;top:0;width:98px;height:2px;background:#e8473a}
  .progress-knob{left:95px;top:-2px;width:6px;height:6px;border-radius:50%;background:#e8473a}
  .hero-actions{left:290px;top:469px;display:flex;gap:17px}
  .btn-outline-light{width:125px;height:31px;border:2px solid var(--white);border-radius:3px;color:var(--white);font-size:14.5px;font-weight:700;display:flex;align-items:center;justify-content:center}

  /* features */
  .features{position:absolute;left:0;top:627px;width:847px;height:308px;background:var(--paper)}
  .feature{top:49px;width:210px;text-align:center}
  .feature-icon{width:54px;height:54px;border-radius:50%;background:var(--green);margin:0 auto;display:flex;align-items:center;justify-content:center}
  .feature-title{margin-top:16px;font-size:12px;font-weight:700;color:var(--ink)}
  .feature-text{margin-top:12px;font-size:8px;line-height:14.5px;color:var(--muted);height:74px}
  .btn-outline-green{margin:10px auto 0;width:82px;height:31px;border:2px solid var(--green);border-radius:3px;font-size:11.5px;font-weight:700;color:var(--ink);display:flex;align-items:center;justify-content:center;background:var(--white)}

  /* contact */
  .contact{position:absolute;left:0;top:935px;width:847px;height:168px;background:linear-gradient(180deg,var(--wood-b),var(--wood-a))}
  .contact-title{left:0;width:847px;top:37px;text-align:center;color:var(--white);font-size:17px;font-weight:700}
  .contact-line{left:0;width:847px;top:68px;text-align:center;color:var(--white);font-size:12.5px}
  .social{left:335px;top:103px;display:flex;gap:9px}
  .social span{width:22px;height:22px;border-radius:50%;background:rgba(255,255,255,.35)}
  .social span.active{background:var(--green)}

  /* footer */
  .site-footer{position:absolute;left:0;top:1103px;width:847px;height:97px;background:var(--footer)}
  .footer-links{left:0;width:847px;top:47px;display:flex;justify-content:center;gap:25px;font-size:11.5px;color:#777}
</style>
</head>
<body>
  <header class="site-header">
    <div class="abs brand"><span class="brand-mark"></span><span class="brand-name">THE FERN GUILD</span></div>
    <nav class="abs main-nav"><span>HOME</span><span>MEMBERSHIP</span><span>CONTACT US</span></nav>
    <a class="abs btn-signup-top">Sign Up</a>
  </header>

  <section class="hero" role="img" aria-label="Close-up photo of a green leaf">
    <h1 class="abs hero-title">WE GROW PLANTS</h1>
    <p class="abs hero-sub">BEAUTIFUL, HEALTY, AFFORDABLE PLANTS</p>

    <div class="abs video">
      <div class="abs video-art" role="img" aria-label="Whiteboard video frame: calendar, presenter and wallet illustrations"></div>
      <p class="abs video-caption">As a loyal customer of<br>The Fern Farm we have saved you money<br>down through the years no</p>
      <div class="abs video-bar">
        <div class="abs track-title">Garden Stroll</div>
        <svg class="abs" style="left:28px;top:16px" width="80" height="16" viewBox="0 0 80 16" fill="#fff">
          <rect x="0" y="3" width="2" height="10"/><polygon points="9,3 2,8 9,13"/><polygon points="16,3 9,8 16,13"/>
          <rect x="30" y="1" width="4" height="14"/><rect x="38" y="1" width="4" height="14"/>
          <polygon points="56,3 63,8 56,13"/><polygon points="63,3 70,8 63,13"/><rect x="70" y="3" width="2" height="10"/>
        </svg>
        <div class="abs time" style="left:129px">00:02:58</div>
        <div class="abs progress"><div class="abs progress-fill"></div><div class="abs progress-knob"></div></div>
        <div class="abs time" style="left:378px">-00:03:23</div>
        <svg class="abs" style="left:428px;top:16px" width="100" height="16" viewBox="0 0 100 16" fill="none" stroke="#fff" stroke-width="1.6">
          <polygon points="1,5 5,5 10,1 10,15 5,11 1,11" fill="#fff"/><path d="M13 5v6M16 3v10"/>
          <path d="M58 5a6 6 0 1 0 1 4"/><polyline points="55,2 58,5 55,7"/>
          <rect x="82" y="2" width="17" height="11"/><path d="M87 15h7"/>
        </svg>
      </div>
    </div>

    <div class="abs hero-actions">
      <a class="btn-outline-light">learn more</a>
      <a class="btn-outline-light">Sign up</a>
    </div>
  </section>

  <section class="features">
    <article class="abs feature" style="left:80px">
      <div class="feature-icon"><svg width="24" height="24" viewBox="0 0 24 24" fill="#fff"><rect x="2" y="10" width="5" height="12"/><path d="M9 10l4-8c2 0 3 1 2.5 4L15 9h6c1 0 2 1 1.5 2.5l-2 9c-.3 1-1 1.5-2 1.5H9z"/></svg></div>
      <h2 class="feature-title">Satisfaction Guaranteed</h2>
      <p class="feature-text">We guarantee our plants to arrive in good, healthy condition labeled true to name. At the time of sale our plants are guaranteed to be free of known hosta viruses, foliar nematodes and disease free perennials . . . .</p>
      <a class="btn-outline-green">Learn more</a>
    </article>
    <article class="abs feature" style="left:319px">
      <div class="feature-icon"><svg width="26" height="26" viewBox="0 0 24 24" fill="#fff"><polygon points="12,2 15,9 22,9.5 16.5,14 18.5,21 12,17 5.5,21 7.5,14 2,9.5 9,9"/></svg></div>
      <h2 class="feature-title">Company History</h2>
      <p class="feature-text">We have been in the nursery business for 30 rears. We got into the mail order business in 2001. We operate one retail garden center and are in the process of constructing a second retail location. There is nothing to see at &nbsp;. . . .</p>
      <a class="btn-outline-green">Learn more</a>
    </article>
    <article class="abs feature" style="left:558px">
      <div class="feature-icon"><svg width="26" height="26" viewBox="0 0 24 24" fill="#fff"><circle cx="12" cy="7" r="5"/><path d="M2 23c0-6 4-9 10-9s10 3 10 9z"/></svg></div>
      <h2 class="feature-title">A Great Customer</h2>
      <p class="feature-text">Have you ever heard the expression "The more I get to know people the more I like my dog"...... if you feel like you fall into that description of people please don't order from us. Running a mail order . . . .</p>
      <a class="btn-outline-green">Learn more</a>
    </article>
  </section>

  <section class="contact" role="img" aria-label="Wooden plank background framed by ivy leaves">
    <h2 class="abs contact-title">Say Hi &amp; Get in Touch</h2>
    <p class="abs contact-line">if you are in Cedar Hill VA stop by and see us. (555-014-2368)</p>
    <div class="abs social"><span></span><span></span><span class="active"></span><span></span><span></span><span></span></div>
  </section>

  <footer class="site-footer">
    <nav class="abs footer-links"><span>Contact</span><span>Download</span><span>Press</span><span>Email</span><span>Support</span><span>Privacy Policy</span></nav>
  </footer>
</body>
</html>
```